50's-style gig poster for a birthday bash

My wife was born in 1957 and is turning 57 next month. I'm throwing a surprise party for her, and thought it would be fun to have a 18x24 poster printed and framed for the event. Attached is a poster from a Rolf Tesker gig in 1957. I'd like something like this, with a tinted B&W head shot of my wife, with similar fonts and background color schemes. The copy will be GRETA at the top (where the name ROLF appears), with 57X57 under it, and the word Celebration where the word Quartet currently appears. The rest of the copy will be provided to you. Thanks for your interest and I look forward to working with you.

```html
<!DOCTYPE html>
<html lang="en">
<head>
<meta charset="utf-8">
<title>GRETA 57X57 Celebration</title>
<link rel="stylesheet" href="https://fonts.googleapis.com/css2?family=Oswald:wght@500&family=Lobster&family=Archivo+Black&family=Alfa+Slab+One&display=swap">
<style>
  :root {
    --cream: #f3e9cf;
    --blue: #39489a;
    --red: #c63a3a;
    --navy: #1c2452;
    --ink: #111;
  }
  * { margin: 0; padding: 0; box-sizing: border-box; }
  html, body { width: 900px; height: 1200px; overflow: hidden; background: var(--cream); }
  .poster { position: relative; width: 900px; height: 1200px; background: var(--cream); overflow: hidden; }

  .stripe { position: absolute; top: 0; bottom: 0; width: 120px; }
  .stripe--blue { background: var(--blue); }
  .stripe--red { background: var(--red); }

  .kicker {
    position: absolute; left: 58px; top: 26px;
    font: 500 46px/1 'Oswald', sans-serif; color: var(--cream);
    text-shadow: 3px 3px 0 var(--navy);
    transform: scaleX(1.3); transform-origin: left top;
  }
  .headline-letter {
    position: absolute; width: 160px; margin-left: -80px; text-align: center;
    font: 500 210px/1 'Oswald', sans-serif; color: var(--cream);
    text-shadow: 6px 6px 0 var(--navy);
    transform: scaleX(1.15);
  }
  .row-name { top: 52px; }
  .row-age { top: 222px; }

  .portrait {
    position: absolute; left: 74px; top: 418px; width: 374px; height: 430px;
    background: #fff; padding: 10px;
    transform: rotate(-3deg);
    box-shadow: -12px 12px 0 var(--ink);
  }
  .portrait-fill {
    width: 100%; height: 100%;
    background: linear-gradient(160deg, #9aa3c4 0%, #5a6592 45%, #1f2440 100%);
  }

  .event-title {
    position: absolute; left: 430px; top: 372px;
    font: 400 86px/1 'Lobster', cursive; color: var(--cream);
    -webkit-text-stroke: 2px var(--navy);
    text-shadow: 4px 4px 0 var(--navy);
    transform: rotate(-9deg);
  }
  .featuring-label {
    position: absolute; left: 535px; top: 478px;
    font: 400 30px/1 'Lobster', cursive; color: var(--cream);
    text-shadow: 2px 2px 0 var(--navy);
  }
  .guest-list {
    position: absolute; left: 480px; top: 524px; width: 330px; list-style: none; text-align: center;
    font: 400 22px/30px 'Archivo Black', sans-serif; color: var(--cream);
    text-shadow: 2px 2px 0 var(--navy);
  }

  .date-badge { position: absolute; left: 480px; top: 722px; width: 332px; height: 196px; }
  .date-badge-text {
    position: absolute; inset: 0; display: flex; flex-direction: column; justify-content: center; align-items: center;
    font: 400 30px/44px 'Archivo Black', sans-serif; color: var(--blue);
  }

  .support-label {
    position: absolute; left: 156px; top: 900px;
    font: 400 32px/1 'Lobster', cursive; color: var(--cream);
    text-shadow: 2px 2px 0 var(--navy);
  }
  .support-act {
    position: absolute; left: 0; right: 0; top: 935px; text-align: center;
    font: 400 74px/1.1 'Lobster', cursive; color: var(--cream);
    -webkit-text-stroke: 1.5px var(--navy);
    text-shadow: 4px 4px 0 var(--navy);
  }

  .venue {
    position: absolute; left: 74px; top: 1036px; width: 762px; height: 110px;
    background: var(--cream); border: 3px solid #bdb39a;
    text-align: center; padding-top: 8px;
  }
  .venue-name {
    font: 400 56px/1.05 'Alfa Slab One', serif; color: var(--red);
    letter-spacing: 2px;
    text-shadow: 3px 3px 0 var(--navy);
  }
  .venue-address {
    font: 400 24px/1.3 'Archivo Black', sans-serif; color: var(--blue);
  }
</style>
</head>
<body>
<main class="poster">
  <div class="stripe stripe--blue" style="left:24px;width:132px"></div>
  <div class="stripe stripe--red" style="left:190px"></div>
  <div class="stripe stripe--blue" style="left:364px"></div>
  <div class="stripe stripe--red" style="left:540px"></div>
  <div class="stripe stripe--blue" style="left:726px"></div>
  <div class="stripe stripe--blue" style="left:872px;width:28px"></div>

  <div class="kicker">THE</div>

  <h1 class="headline" aria-label="GRETA 57X57">
    <span class="headline-letter row-name" style="left:94px">G</span>
    <span class="headline-letter row-name" style="left:250px">R</span>
    <span class="headline-letter row-name" style="left:424px">E</span>
    <span class="headline-letter row-name" style="left:600px">T</span>
    <span class="headline-letter row-name" style="left:786px">A</span>
    <span class="headline-letter row-age" style="left:94px">5</span>
    <span class="headline-letter row-age" style="left:250px">7</span>
    <span class="headline-letter row-age" style="left:424px">X</span>
    <span class="headline-letter row-age" style="left:600px">5</span>
    <span class="headline-letter row-age" style="left:786px">7</span>
  </h1>

  <figure class="portrait">
    <div class="portrait-fill" role="img" aria-label="Blue-tinted black and white head shot of Greta, smiling"></div>
  </figure>

  <h2 class="event-title">Celebration</h2>
  <p class="featuring-label">Featuring:</p>
  <ul class="guest-list">
    <li>The Marlowes</li>
    <li>The Fennimores</li>
    <li>The Pelletiers</li>
    <li>The Ashby-Coopers</li>
    <li>The Trevors</li>
    <li>The Whitcombs</li>
  </ul>

  <div class="date-badge">
    <svg width="332" height="196" viewBox="0 0 332 196" aria-hidden="true">
      <ellipse cx="166" cy="98" rx="162" ry="94" fill="#f3e9cf" stroke="#111" stroke-width="4"/>
    </svg>
    <div class="date-badge-text">
      <span>One Night Only</span>
      <span>April 4, 2014</span>
      <span>6:00 PM</span>
    </div>
  </div>

  <p class="support-label">Also Appearing</p>
  <p class="support-act">The Larks &amp; Nell Ostrow</p>

  <section class="venue">
    <p class="venue-name">BISTRO MARCEL</p>
    <p class="venue-address">418 Cedar Lane, Harmon Springs, California</p>
  </section>
</main>
</body>
</html>
```